Business Card Design

We need a business card for a new business based in Sydney, Australia. It is a home based baking business, the key products are cookies and muffins and slices including gluten free baked goods. With the emphasis on home made baking. The target market is cafes, coffee shops and vans, restaurants. Products may be provided in display jars or individually wrapped. The final design should be in the colours pink, purple.

Business

Tindle's Bakery Pty Ltd, Marisa Pellow, marisa@tindlesbakery.com.au
0451 276 308, www.tindlesbakery.com.au, ACN 512 648 397,

```html
<!DOCTYPE html>
<html lang="en">
<head>
<meta charset="utf-8">
<title>Tindle's Bakery Pty Ltd — Business Card</title>
<link rel="stylesheet" href="https://fonts.googleapis.com/css2?family=Bowlby+One&family=Great+Vibes&family=Cousine&display=swap">
<style>
  :root {
    --backdrop: #efece8;
    --card: #ffffff;
    --berry-red: #d3232b;
    --candy-pink: #ee6a9f;
    --blush: #f8c6d8;
    --placeholder-top: #f3b3cb;
    --placeholder-bottom: #f9dbe6;
  }
  html, body {
    margin: 0;
    width: 1200px;
    height: 918px;
    overflow: hidden;
    background: var(--backdrop);
  }
  .canvas {
    position: relative;
    width: 1200px;
    height: 918px;
  }
  .business-card {
    position: absolute;
    left: 100px;
    top: 174px;
    width: 1000px;
    height: 570px;
    background: var(--card);
    box-shadow: 0 6px 24px rgba(0,0,0,0.12);
    overflow: hidden;
  }
  .stripe-border {
    position: absolute;
    background: linear-gradient(135deg, var(--berry-red), var(--candy-pink) 45%, var(--blush));
  }
  .stripe-border--left { left: 0; top: 0; width: 42px; height: 570px; }
  .stripe-border--top { left: 0; top: 0; width: 440px; height: 38px; }
  .stripe-border--right { right: 0; top: 0; width: 42px; height: 570px; }
  .stripe-border--bottom { right: 0; bottom: 0; width: 560px; height: 38px; }
  .cupcake-illustration {
    position: absolute;
    left: 70px;
    top: 70px;
    width: 310px;
    height: 430px;
    border-radius: 16px;
    background: linear-gradient(180deg, var(--placeholder-top), var(--placeholder-bottom));
  }
  .card-details {
    position: absolute;
    left: 420px;
    top: 96px;
    width: 520px;
    text-align: center;
    color: var(--berry-red);
  }
  .company-name {
    margin: 0;
    font-family: "Bowlby One", sans-serif;
    font-size: 40px;
    line-height: 1.08;
    letter-spacing: 1px;
    font-weight: 400;
    text-transform: uppercase;
  }
  .person-name {
    margin: 10px 0 14px;
    font-family: "Great Vibes", cursive;
    font-size: 56px;
    line-height: 1.1;
    font-weight: 400;
  }
  .contact-line {
    margin: 0;
    font-family: "Cousine", monospace;
    line-height: 1.35;
  }
  .contact-line--large { font-size: 32px; }
  .contact-line--small { font-size: 23px; }
</style>
</head>
<body>
<main class="canvas">
  <section class="business-card">
    <div class="stripe-border stripe-border--left" role="img" aria-label="Red and pink candy stripe border"></div>
    <div class="stripe-border stripe-border--top" role="img" aria-label="Red and pink candy stripe border"></div>
    <div class="stripe-border stripe-border--right" role="img" aria-label="Red and pink candy stripe border"></div>
    <div class="stripe-border stripe-border--bottom" role="img" aria-label="Red and pink candy stripe border"></div>

    <div class="cupcake-illustration" role="img" aria-label="Illustration of a chocolate cupcake with sprinkles and a cherry on a red cake stand"></div>

    <div class="card-details">
      <h1 class="company-name">Tindle's<br>Bakery Pty Ltd</h1>
      <p class="person-name">Marisa Pellow</p>
      <p class="contact-line contact-line--large">0451 276 308</p>
      <p class="contact-line contact-line--large">ACN 512 648 397</p>
      <p class="contact-line contact-line--small">marisa@tindlesbakery.com.au</p>
      <p class="contact-line contact-line--small">www.tindlesbakery.com.au</p>
    </div>
  </section>
</main>
</body>
</html>
```